Corvane Bookkeeping Services business cards

looking for a double sided business card design. My logo is attached. I am looking for a design similar to the attached. Keen to see what my logo in white on the blue background would look like.

```html
<!DOCTYPE html>
<html lang="en">
<head>
<meta charset="utf-8">
<title>Corvane Bookkeeping Services – Business Cards</title>
<link rel="stylesheet" href="https://fonts.googleapis.com/css2?family=Montserrat:wght@400;500;800&display=swap">
<style>
  :root {
    --navy: #033570;
    --green: #9bbb2a;
    --white: #ffffff;
    --stage: #3a3a3c;
    --divider: #6d84a8;
  }
  * { box-sizing: border-box; margin: 0; padding: 0; }
  html, body { width: 1200px; height: 1200px; overflow: hidden; }
  body {
    background: var(--stage);
    font-family: "Montserrat", Arial, sans-serif;
    display: flex;
    flex-direction: column;
    align-items: center;
    justify-content: center;
    gap: 60px;
  }
  .card {
    width: 840px;
    height: 480px;
    border-radius: 34px;
    overflow: hidden;
    position: relative;
  }

  /* Front */
  .card-front { background: var(--navy); }
  .front-top {
    position: absolute; left: 0; top: 0; width: 100%; height: 205px;
    background: var(--white);
    display: flex; align-items: center; justify-content: center;
  }
  .front-stripe {
    position: absolute; left: 0; top: 205px; width: 100%; height: 10px;
    background: var(--green);
  }
  .brand { display: flex; align-items: center; gap: 18px; }
  .brand-mark { width: 46px; height: 46px; background: var(--green); }
  .brand-name {
    font-weight: 800; font-size: 44px; letter-spacing: 0.5px;
    color: var(--navy); line-height: 1.05;
  }
  .brand-name small { display: block; font-size: 19px; letter-spacing: 3px; }

  .person { position: absolute; left: 62px; top: 318px; }
  .person-name { color: var(--green); font-weight: 500; font-size: 40px; line-height: 1; }
  .person-role { color: var(--white); font-weight: 400; font-size: 22px; margin-top: 6px; }

  .divider {
    position: absolute; left: 408px; top: 258px; width: 1px; height: 180px;
    background: var(--divider);
  }
  .contacts {
    position: absolute; left: 446px; top: 262px;
    list-style: none; color: var(--white); font-size: 19px; line-height: 1.2;
  }
  .contacts li { display: flex; align-items: flex-start; gap: 12px; margin-bottom: 10px; }
  .contacts svg { width: 22px; height: 22px; flex: none; margin-top: 1px; }

  /* Back */
  .card-back {
    background: var(--navy);
    display: flex; align-items: center; justify-content: center;
  }
  .card-back .brand-mark { width: 64px; height: 64px; background: var(--white); }
  .card-back .brand-name { color: var(--white); font-size: 62px; }
  .card-back .brand-name small { font-size: 26px; letter-spacing: 4px; }
</style>
</head>
<body>
  <section class="card card-front">
    <div class="front-top">
      <div class="brand">
        <span class="brand-mark"></span>
        <span class="brand-name">Corvane<small>BOOKKEEPING SERVICES</small></span>
      </div>
    </div>
    <div class="front-stripe"></div>

    <div class="person">
      <p class="person-name">FULL NAME</p>
      <p class="person-role">POSITION</p>
    </div>

    <div class="divider"></div>

    <ul class="contacts">
      <li>
        <svg viewBox="0 0 24 24"><path fill="#9bbb2a" d="M6.6 10.8a15 15 0 0 0 6.6 6.6l2.2-2.2c.3-.3.7-.4 1-.2 1.1.4 2.3.6 3.6.6.6 0 1 .4 1 1V20c0 .6-.4 1-1 1A17 17 0 0 1 3 4c0-.6.4-1 1-1h3.5c.6 0 1 .4 1 1 0 1.3.2 2.5.6 3.6.1.3 0 .7-.2 1z"/></svg>
        <span>(000) 000 0000</span>
      </li>
      <li>
        <svg viewBox="0 0 24 24"><rect x="2" y="5" width="20" height="14" rx="1" fill="#9bbb2a"/><path d="M2 6l10 7 10-7" fill="none" stroke="#033570" stroke-width="1.8"/></svg>
        <span>email@company.com</span>
      </li>
      <li>
        <svg viewBox="0 0 24 24" fill="none" stroke="#9bbb2a" stroke-width="1.8"><circle cx="12" cy="12" r="9.5"/><ellipse cx="12" cy="12" rx="4" ry="9.5"/><path d="M2.5 12h19M4 7h16M4 17h16"/></svg>
        <span>www.company.com</span>
      </li>
      <li>
        <svg viewBox="0 0 24 24"><path fill="#9bbb2a" d="M12 2a7 7 0 0 0-7 7c0 5 7 13 7 13s7-8 7-13a7 7 0 0 0-7-7zm0 9.5A2.5 2.5 0 1 1 12 6.5a2.5 2.5 0 0 1 0 5z"/></svg>
        <span>123 Name Street, 000<br>Your City, 00000-000</span>
      </li>
    </ul>
  </section>

  <section class="card card-back">
    <div class="brand">
      <span class="brand-mark"></span>
      <span class="brand-name">Corvane<small>BOOKKEEPING SERVICES</small></span>
    </div>
  </section>
</body>
</html>
```